Brand new leaflet design creative ideas.

I need a flyer designed for my business

I run a pay weekly carpet business and need designs for a flyer this design i will also want to enable it on letterheads business cards and a logo from it when created.

my domain name is www.pebblemarsh.co.uk / www.pebblemarsh.com

Our main competitor i have attached his design to this brief to give you a bit of an idea on how we work, however i do not want a copycat design i want a brand new design something not like theres but eye catching direct to the point.

We are open to colour suggestions as long as the colours work.
Thank you.

Target Market(s)

This print material will be delivered to customers houses.

Industry/Entity Type

Flooring

Font styles to use
Serif
Sans Serif

Requirements
Must have
• Website domain name,
• Various print options CMYK, PDF
Nice to have
• Creativity eye catching
Should not have
• SHOULD NOT BE A COPYCAT DESIGN SOMETHING NEW & CREATIVE

```html
<!DOCTYPE html>
<html lang="en">
<head>
<meta charset="utf-8">
<title>Pebblemarsh – Pay Weekly Carpet &amp; Vinyls Flyer</title>
<link rel="stylesheet" href="https://fonts.googleapis.com/css2?family=Bebas+Neue&family=Oswald:wght@600;700&family=Open+Sans:wght@400;600;700;800&family=Playfair+Display+SC:wght@700&family=Lobster+Two:ital,wght@1,700&family=Poiret+One&family=Alfa+Slab+One&family=Playfair+Display:ital,wght@1,900&display=swap">
<style>
  :root {
    --yellow: #fdd20e;
    --red: #ec2227;
    --wine: #a8232a;
    --dark: #3a3a3a;
    --ink: #111;
    --paper: #ebebeb;
    --pink: #f6a3a3;
    --white: #fff;
  }
  * { box-sizing: border-box; margin: 0; padding: 0; }
  html, body { width: 962px; height: 1200px; overflow: hidden; background: var(--paper); }
  .flyer { position: relative; width: 962px; height: 1200px; background: var(--paper); overflow: hidden; font-family: "Open Sans", sans-serif; }

  .hero-photo { position: absolute; left: 0; top: 52px; width: 962px; height: 360px;
    background: radial-gradient(ellipse at 70% 55%, #c9bcaf 0%, #a89a8d 35%, #8f8276 70%, #a69a8f 100%); }
  .hero-top-band { position: absolute; left: 0; top: 0; width: 962px; height: 52px; background: var(--paper); }

  .keep-banner { position: absolute; left: 0; top: 0; width: 560px; height: 168px; }
  .keep-banner svg { position: absolute; inset: 0; }
  .keep-text { position: absolute; left: 18px; top: 24px; font-family: "Bebas Neue", sans-serif; line-height: 0.98; white-space: nowrap; }
  .keep-text .line-1 { color: var(--wine); font-size: 60px; }
  .keep-text .line-1 small { font-size: 26px; vertical-align: 26px; margin-left: 4px; }
  .keep-text .line-2 { color: var(--ink); font-size: 49px; }

  .brand { position: absolute; left: 540px; top: 165px; width: 400px; display: flex; align-items: center; gap: 14px; white-space: nowrap; }
  .brand-dot { width: 46px; height: 46px; border-radius: 50%; background: var(--red); flex: none; }
  .brand-name { font-family: "Open Sans", sans-serif; font-weight: 800; font-size: 42px; line-height: 1; color: var(--ink); }

  .offer-band { position: absolute; left: 0; top: 405px; width: 962px; height: 194px; background: var(--yellow); }
  .buy-now { position: absolute; left: 0; top: 405px; width: 311px; height: 194px; text-align: center; padding-top: 36px; line-height: 0.98; }
  .buy-now .l1 { font-family: "Oswald", sans-serif; font-weight: 700; font-size: 66px; color: var(--red); letter-spacing: 1px; }
  .buy-now .l2 { font-family: "Oswald", sans-serif; font-weight: 700; font-size: 52px; color: var(--ink); }

  .welcome-box { position: absolute; left: 311px; top: 376px; width: 351px; height: 223px; }
  .welcome-box svg { position: absolute; inset: 0; }
  .welcome-text { position: absolute; left: 0; top: 0; width: 351px; text-align: center; padding-top: 4px; line-height: 1; }
  .welcome-text .greet { font-family: "Playfair Display SC", serif; font-weight: 700; font-size: 44px; color: var(--yellow); }
  .welcome-text .area { font-family: "Open Sans", sans-serif; font-weight: 800; font-size: 42px; color: var(--ink); line-height: 1.08; margin-top: 4px; }

  .call-now { position: absolute; left: 662px; top: 405px; width: 300px; height: 194px; text-align: center; padding-top: 28px; }
  .call-now .script { font-family: "Lobster Two", cursive; font-style: italic; font-weight: 700; font-size: 46px; line-height: 0.98; color: var(--ink); }
  .call-now .cta { font-family: "Open Sans", sans-serif; font-weight: 700; font-size: 40px; color: var(--red); margin-top: 8px; }

  .deals-ribbon { position: absolute; left: 27px; top: 630px; width: 445px; height: 96px; }
  .deals-ribbon svg { position: absolute; inset: 0; }
  .deals-title { position: absolute; left: 0; top: 18px; width: 445px; text-align: center; font-family: "Oswald", sans-serif; font-weight: 600; font-size: 31px; letter-spacing: 0.5px; color: var(--ink); white-space: nowrap; }
  .deals-list { position: absolute; left: 56px; top: 704px; width: 389px; height: 363px; background: var(--dark); list-style: none; padding: 36px 0 0 17px; }
  .deals-list li { display: flex; align-items: center; gap: 5px; color: var(--white); font-size: 28.5px; line-height: 38px; white-space: nowrap; }
  .deals-list li svg { width: 14px; height: 14px; flex: none; }
  .deals-list b { font-weight: 600; }

  .headline { position: absolute; left: 497px; top: 718px; width: 450px; white-space: nowrap; }
  .headline .pay { font-family: "Poiret One", sans-serif; font-size: 86px; line-height: 1; color: var(--ink); font-variant: small-caps; font-weight: 400; -webkit-text-stroke: 1.5px var(--ink); }
  .headline .carpet { font-family: "Alfa Slab One", serif; font-size: 90px; line-height: 1; color: var(--wine); margin-top: 4px; letter-spacing: 1px; }
  .headline .vinyls { font-family: "Playfair Display", serif; font-style: italic; font-weight: 900; font-size: 76px; line-height: 1; color: var(--wine); text-align: right; margin-top: 4px; }

  .footer { position: absolute; left: 0; top: 1088px; width: 962px; height: 112px; }
  .footer svg.footer-shapes { position: absolute; inset: 0; }
  .phone-icon { position: absolute; left: 26px; top: 18px; width: 74px; height: 74px; }
  .call-us { position: absolute; left: 119px; top: 16px; color: var(--white); font-weight: 700; line-height: 1.2; white-space: nowrap; }
  .call-us .label { font-size: 29px; letter-spacing: 1.5px; }
  .call-us .number { font-size: 29px; font-weight: 600; letter-spacing: 1px; }
  .web { position: absolute; left: 483px; top: 44px; display: flex; align-items: center; gap: 18px; color: var(--white); font-family: "Oswald", sans-serif; font-weight: 600; font-size: 42px; line-height: 1; white-space: nowrap; }
  .web svg { width: 38px; height: 38px; }
</style>
</head>
<body>
<svg width="0" height="0" style="position:absolute">
  <symbol id="tick" viewBox="0 0 14 14">
    <circle cx="7" cy="7" r="6.5" fill="#fff"/>
    <path d="M3.8 7.2 L6.1 9.4 L10.3 4.6" fill="none" stroke="#ec2227" stroke-width="2" stroke-linecap="round" stroke-linejoin="round"/>
  </symbol>
</svg>

<main class="flyer">
  <div class="hero-top-band"></div>
  <div class="hero-photo" role="img" aria-label="Photo of a rolled-up shaggy carpet in warm brown tones"></div>

  <div class="keep-banner">
    <svg viewBox="0 0 560 168" preserveAspectRatio="none">
      <polygon points="0,0 493,0 450,168 0,168" fill="#fdd20e"/>
      <polygon points="493,0 553,52 480,52" fill="#3a3a3a"/>
    </svg>
    <div class="keep-text">
      <div class="line-1">Keep this flyer safe<small>or</small></div>
      <div class="line-2">Share with your buddies</div>
    </div>
  </div>

  <div class="brand">
    <span class="brand-dot"></span>
    <span class="brand-name">Pebblemarsh</span>
  </div>

  <div class="offer-band"></div>

  <div class="buy-now">
    <div class="l1">BUY NOW</div>
    <div class="l2">PAY LATER</div>
  </div>

  <div class="welcome-box">
    <svg viewBox="0 0 351 223" preserveAspectRatio="none">
      <polygon points="0,29 14,0 14,197 0,223" fill="#f6a3a3"/>
      <polygon points="337,0 351,29 351,223 337,197" fill="#f6a3a3"/>
      <rect x="14" y="0" width="323" height="197" fill="#ec2227"/>
      <polygon points="14,197 337,197 351,223 0,223" fill="#3a3a3a"/>
    </svg>
    <div class="welcome-text">
      <div class="greet">Welcome!</div>
      <div class="area">WE’RE IN<br>YOUR<br>AREA</div>
    </div>
  </div>

  <div class="call-now">
    <div class="script">Don’t<br>Miss it,</div>
    <div class="cta">CALL NOW</div>
  </div>

  <div class="deals-ribbon">
    <svg viewBox="0 0 445 96" preserveAspectRatio="none">
      <defs>
        <linearGradient id="ribbonFill" x1="0" y1="0" x2="0" y2="1">
          <stop offset="0" stop-color="#fdd20e"/>
          <stop offset="0.45" stop-color="#f27a1f"/>
          <stop offset="1" stop-color="#ec2227"/>
        </linearGradient>
      </defs>
      <polygon points="0,74 29,74 29,96" fill="#f6a3a3"/>
      <polygon points="416,74 445,74 416,96" fill="#f6a3a3"/>
      <rect x="0" y="0" width="445" height="78" fill="url(#ribbonFill)"/>
    </svg>
    <div class="deals-title">OUR AMAZING CARPET DEALS</div>
  </div>

  <ul class="deals-list">
    <li><svg><use href="#tick"/></svg>Pay only <b>£10.00/week</b></li>
    <li><svg><use href="#tick"/></svg><b>£500</b> credit limit</li>
    <li><svg><use href="#tick"/></svg>Interest <b>FREE</b></li>
    <li><svg><use href="#tick"/></svg><b>NO</b> Credit Checks</li>
    <li><svg><use href="#tick"/></svg><b>FREE</b> Underlay</li>
    <li><svg><use href="#tick"/></svg><b>FREE</b> Grippers</li>
    <li><svg><use href="#tick"/></svg><b>FREE</b> Door Trims</li>
    <li><svg><use href="#tick"/></svg><b>FREE</b> Home Measuring</li>
  </ul>

  <div class="headline">
    <div class="pay">Pay Weekly</div>
    <div class="carpet">CARPET</div>
    <div class="vinyls">&amp; Vinyls</div>
  </div>

  <footer class="footer">
    <svg class="footer-shapes" viewBox="0 0 962 112" preserveAspectRatio="none">
      <polygon points="440,0 457,0 470,22" fill="#f6a3a3"/>
      <rect x="440" y="22" width="522" height="90" fill="#3a3a3a"/>
      <polygon points="0,0 445,0 372,112 0,112" fill="#ec2227"/>
    </svg>
    <svg class="phone-icon" viewBox="0 0 24 24">
      <path fill="#fff" d="M6.6 10.8c1.4 2.8 3.8 5.1 6.6 6.6l2.2-2.2c.3-.3.7-.4 1-.2 1.1.4 2.3.6 3.6.6.6 0 1 .4 1 1V20c0 .6-.4 1-1 1C10.6 21 3 13.4 3 4c0-.6.4-1 1-1h3.5c.6 0 1 .4 1 1 0 1.3.2 2.5.6 3.6.1.3 0 .7-.2 1l-2.3 2.2z"/>
    </svg>
    <div class="call-us">
      <div class="label">CALL US TODAY</div>
      <div class="number">+800 0456 789</div>
    </div>
    <div class="web">
      <svg viewBox="0 0 24 24" fill="none" stroke="#fff" stroke-width="1.6">
        <circle cx="12" cy="12" r="10"/>
        <ellipse cx="12" cy="12" rx="4.5" ry="10"/>
        <line x1="2" y1="12" x2="22" y2="12"/>
        <path d="M4 6.5h16M4 17.5h16"/>
      </svg>
      <span>www.pebblemarsh.co.uk</span>
    </div>
  </footer>
</main>
</body>
</html>
```